Barrister Letterhead incorporating existing logo/design

Require new letterhead template to incorporate logo and information on 'Letter 2015' word document. Currently the information on the letterhead is very busy and would like a cleaner look.
Must look good in black and white, and colour when printed.

Target Market(s)

Professional

Industry/Entity Type

Legal

Requirements
Must have
• Clean professional look.

```html
<!DOCTYPE html>
<html lang="en">
<head>
<meta charset="utf-8">
<title>Ashford Chambers Letterhead</title>
<link rel="stylesheet" href="https://fonts.googleapis.com/css2?family=EB+Garamond:wght@400;500&family=Tinos&display=swap">
<style>
  :root {
    --navy: #1b2848;
    --grey: #8a8d92;
    --ink: #2b2b2b;
    --rule: #d9dadc;
    --paper: #ffffff;
    --backdrop: #ececec;
  }
  * { box-sizing: border-box; margin: 0; padding: 0; }
  html, body {
    width: 1200px;
    height: 1172px;
    overflow: hidden;
    background: var(--backdrop);
  }
  .letterhead {
    position: absolute;
    left: 185px;
    top: 0;
    width: 830px;
    height: 1172px;
    background: var(--paper);
  }
  .masthead {
    position: absolute;
    top: 62px;
    left: 0;
    width: 100%;
    display: flex;
    justify-content: center;
    align-items: center;
    gap: 12px;
  }
  .masthead-square {
    width: 64px;
    height: 58px;
    background: var(--navy);
  }
  .masthead-text {
    display: flex;
    flex-direction: column;
  }
  .firm-name {
    font-family: "EB Garamond", serif;
    font-weight: 500;
    font-size: 33px;
    line-height: 1;
    letter-spacing: 0.5px;
    color: var(--navy);
    padding-bottom: 4px;
    border-bottom: 1px solid var(--rule);
  }
  .firm-tagline {
    font-family: "EB Garamond", serif;
    font-weight: 400;
    font-size: 22px;
    line-height: 1.1;
    letter-spacing: 2px;
    color: var(--grey);
    padding-top: 2px;
  }
  .contact-block {
    position: absolute;
    top: 160px;
    left: 0;
    width: 100%;
    text-align: center;
    font-family: "Tinos", serif;
    font-size: 10px;
    line-height: 13.6px;
    color: var(--ink);
  }
  .contact-block .sep { padding: 0 8px; }
  .header-rule {
    position: absolute;
    top: 247px;
    left: 92px;
    width: 645px;
    height: 1px;
    background: var(--rule);
  }
  .footer-band {
    position: absolute;
    left: 0;
    bottom: 0;
    width: 100%;
    height: 41px;
    background: var(--navy);
  }
</style>
</head>
<body>
  <main class="letterhead">
    <header class="masthead">
      <div class="masthead-square"></div>
      <div class="masthead-text">
        <div class="firm-name">ASHFORD CHAMBERS</div>
        <div class="firm-tagline">Barristers and Mediators</div>
      </div>
    </header>
    <address class="contact-block" style="font-style:normal">
      <div>LEVEL 1 42 HARBOUR STREET, KESTREL BAY</div>
      <div>P.O. BOX 218, KESTREL BAY. Q. 4900</div>
      <div>TELEPHONE 07 4000 0123<span class="sep">|</span>FAX 07 4000 0456</div>
      <div>Email clerk@ashfordchambers.example<span class="sep">|</span>www.ashfordchambers.example</div>
      <div>ABN 00 000 000 000</div>
    </address>
    <div class="header-rule"></div>
    <footer class="footer-band"></footer>
  </main>
</body>
</html>
```